Webpage for a treatment housing for young addicts.

I need a new design and files for my wordpress page. I need it to be more neat and clean. I need it to look professional with a starting page that will work as a navigation. I need like logo and phone number and such up top, a picture under it with one sentence as a slogan and under it 6 boxes to click to come to our different pages. Under it I want news etc.

Target Market(s)

Social services, employees and governements

Coding

Coded - Design and coding required

Font styles to use
Sans Serif

Colors
abd037
3176b5
9d9d9d
aaaaaa
f04a50

Requirements
Must have
• A nice design
Nice to have
• need it to look professional with a starting page that will work as a navigation. I need like logo and phone number and such up top, a picture under it with one sentence as a slogan and under it 6 boxes to click to come to our different pages. Under it I want news etc.
• today www.kolrev.se
• want more like www.tralvik.se or www.bersona.se
Should not have
• To many different colours and a messy design.

```html
<!DOCTYPE html>
<html lang="en">
<head>
<meta charset="utf-8">
<title>Kolrev – Treatment housing</title>
<link href="https://fonts.googleapis.com/css2?family=Montserrat:wght@400;500;600;700&family=Open+Sans:wght@400;600&display=swap" rel="stylesheet">
<style>
:root{
  --green:#abd037;
  --blue:#3176b5;
  --navy:#1f4e86;
  --grey:#9d9d9d;
  --grey-light:#aaaaaa;
  --red:#f04a50;
  --bg-soft:#ececec;
  --text:#4a4a4a;
  --white:#ffffff;
}
*{box-sizing:border-box;margin:0;padding:0}
html,body{width:1200px;height:3212px;overflow:hidden}
body{font-family:"Open Sans",Arial,sans-serif;color:var(--text);background:var(--white);position:relative}
h1,h2,h3,h4,.nav,.btn{font-family:"Montserrat",Arial,sans-serif}

/* header */
.site-header{position:absolute;top:0;left:0;width:1200px;height:88px}
.brand{position:absolute;left:164px;top:18px;display:flex;align-items:center;gap:12px}
.brand-dot{width:44px;height:44px;border-radius:50%;background:var(--blue)}
.brand-name{font-family:"Montserrat",sans-serif;font-weight:700;font-size:30px;color:var(--blue)}
.phone{position:absolute;right:164px;top:14px;font-family:"Montserrat",sans-serif;font-weight:600;font-size:17px;color:var(--navy);display:flex;align-items:center;gap:6px}
.nav{position:absolute;right:164px;top:56px;display:flex;gap:30px;font-size:13px;font-weight:700;color:var(--navy);letter-spacing:.3px}

/* hero */
.hero{position:absolute;top:88px;left:0;width:1200px;height:580px;background:linear-gradient(120deg,#c9c3bb 0%,#8f8a86 45%,#5c5a5d 100%)}
.hero h1{position:absolute;top:210px;width:100%;text-align:center;color:var(--white);font-size:41px;font-weight:600;line-height:1.15;letter-spacing:.5px}
.hero-curve{position:absolute;left:0;top:560px;width:1200px;height:140px}
.hero-badge{position:absolute;left:574px;top:612px;width:52px;height:52px;border-radius:50%;background:var(--white);border:3px solid var(--green)}

/* service boxes */
.services{position:absolute;top:732px;left:164px;width:880px;display:grid;grid-template-columns:repeat(3,288px);gap:8px 8px}
.service{height:232px;background:var(--white);border:1px solid #dedede;box-shadow:0 2px 6px rgba(0,0,0,.08);text-align:center;padding-top:30px;position:relative}
.service svg.icon{width:48px;height:48px;stroke:var(--blue);fill:none;stroke-width:2}
.service h3{font-size:15px;font-weight:700;color:var(--navy);margin-top:10px}
.service p{font-size:11px;line-height:1.45;color:var(--grey);width:200px;margin:8px auto 0}
.service .go{position:absolute;left:127px;bottom:18px;width:34px;height:34px;border-radius:50%;background:var(--red)}
.service.featured{background:linear-gradient(180deg,var(--green) 0%,var(--blue) 100%);border:none}
.service.featured svg.icon{stroke:var(--white)}
.service.featured h3,.service.featured p{color:var(--white)}

/* news */
.news{position:absolute;top:1288px;left:0;width:1200px;height:472px;background:var(--bg-soft)}
.section-title{font-size:24px;font-weight:700;color:var(--navy)}
.news .section-title{position:absolute;left:164px;top:52px}
.news .rule{position:absolute;left:164px;top:90px;width:80px;height:3px;background:var(--green)}
.news-list{position:absolute;left:164px;top:120px;display:grid;grid-template-columns:repeat(3,288px);gap:8px}
.news-card{height:232px;background:var(--white);box-shadow:0 2px 6px rgba(0,0,0,.08)}
.news-photo{height:106px;background:linear-gradient(120deg,#d8cfc6,#8a8480)}
.news-body{padding:12px 14px}
.news-date{font-size:11px;color:var(--grey)}
.news-card h4{font-size:14px;font-weight:700;color:var(--navy);margin:4px 0 6px}
.news-card p{font-size:10px;line-height:1.45;color:var(--grey)}
.read-more{display:block;font-family:"Montserrat",sans-serif;font-size:10px;font-weight:700;color:var(--green);margin-top:8px}

/* testimonials */
.testimonials{position:absolute;top:1820px;left:0;width:1200px;height:440px;background:linear-gradient(90deg,var(--blue) 0%,#4c9d8c 50%,var(--green) 100%);color:var(--white);text-align:center}
.testimonials h2{font-size:26px;font-weight:700;margin-top:76px}
.testimonials .rule{width:70px;height:3px;background:var(--white);margin:10px auto 0}
.quote-mark{font-family:"Montserrat",sans-serif;font-size:90px;line-height:1;height:64px;margin-top:22px}
.testimonials blockquote{width:620px;margin:10px auto 0;font-size:18px;line-height:1.5}
.author{font-family:"Montserrat",sans-serif;font-weight:700;font-size:14px;margin-top:18px;letter-spacing:.5px}
.arrow{position:absolute;top:204px;width:30px;height:30px;stroke:var(--white);stroke-width:3;fill:none}

/* work with us */
.careers{position:absolute;top:2320px;left:164px;width:884px;height:440px;background:linear-gradient(135deg,#c7b8a8 0%,#9b8a7c 50%,#6f6a66 100%)}
.hexagon{position:absolute;left:528px;top:44px;width:320px;height:350px}
.hex-content{position:absolute;left:560px;top:130px;width:256px;text-align:center;color:var(--white)}
.hex-content h2{font-size:24px;font-weight:700}
.hex-content p{font-size:12px;line-height:1.5;margin-top:14px}
.btn-outline{display:inline-block;margin-top:20px;padding:10px 30px;border:2px solid var(--white);font-size:12px;font-weight:700;letter-spacing:.6px}

/* footer */
.site-footer{position:absolute;top:2820px;left:0;width:1200px;height:340px;background:var(--bg-soft)}
.footer-brand{position:absolute;left:164px;top:70px;display:flex;align-items:center;gap:12px}
.footer-col{position:absolute;top:60px}
.footer-col h4{font-size:16px;font-weight:700;color:var(--navy);margin-bottom:12px}
.footer-col li{list-style:none;font-size:13px;line-height:1.7;color:var(--text)}
.social{display:flex;gap:14px;margin-top:10px}
.social span{width:18px;height:18px;border-radius:50%;background:var(--blue)}
.newsletter-input{width:240px;height:40px;border:1px solid #d0d0d0;background:var(--white);font-size:12px;color:var(--grey);padding:12px}
.btn-red{display:inline-block;margin-top:12px;background:var(--red);color:var(--white);font-size:12px;font-weight:700;padding:11px 22px;letter-spacing:.5px}
.copyright{position:absolute;top:3160px;left:0;width:1200px;height:52px;background:var(--white);border-top:1px solid #ddd;text-align:center;font-size:12px;line-height:52px;color:var(--grey)}
</style>
</head>
<body>

<header class="site-header">
  <div class="brand"><span class="brand-dot"></span><span class="brand-name">Kolrev</span></div>
  <div class="phone">
    <svg width="16" height="16" viewBox="0 0 24 24" fill="currentColor"><path d="M6.6 10.8a15 15 0 0 0 6.6 6.6l2.2-2.2c.3-.3.7-.4 1-.2 1.1.4 2.3.6 3.6.6.6 0 1 .4 1 1V20c0 .6-.4 1-1 1A17 17 0 0 1 3 4c0-.6.4-1 1-1h3.5c.6 0 1 .4 1 1 0 1.3.2 2.5.6 3.6.1.3 0 .7-.2 1z"/></svg>
    010-4471930
  </div>
  <nav class="nav"><span>ABOUT KOLREV</span><span>EKBACKEN KOLREV</span><span>WORK WITH US</span><span>PLUG</span></nav>
</header>

<section class="hero" role="img" aria-label="Photo of two young women talking together in a bright room">
  <h1>WE CREATE SUSTAINABLE ROADS<br>TO A BETTER FUTURE</h1>
</section>
<svg class="hero-curve" viewBox="0 0 1200 140" preserveAspectRatio="none">
  <path d="M0 0 Q600 150 1200 0 L1200 140 L0 140 Z" fill="#ffffff"/>
  <path d="M0 0 Q600 150 1200 0" fill="none" stroke="#abd037" stroke-width="6"/>
</svg>
<div class="hero-badge"></div>

<section class="services">
  <div class="service featured">
    <svg class="icon" viewBox="0 0 48 48"><circle cx="24" cy="12" r="6"/><path d="M6 38 Q16 30 24 34 L36 30 Q42 30 40 36 L28 42 L6 42"/></svg>
    <h3>PERSONAL ASSISTANCE</h3>
    <p>Class aptent taciti sociosqu ad litora torquent per conubia nostra inceptos</p>
    <span class="go"></span>
  </div>
  <div class="service">
    <svg class="icon" viewBox="0 0 48 48"><circle cx="24" cy="15" r="8"/><path d="M8 42 Q8 27 24 27 Q40 27 40 42 Z"/></svg>
    <h3>INDIVIDUAL</h3>
    <p>Class aptent taciti sociosqu ad litora torquent per conubia nostra inceptos</p>
    <span class="go"></span>
  </div>
  <div class="service">
    <svg class="icon" viewBox="0 0 48 48"><circle cx="14" cy="12" r="5"/><circle cx="34" cy="12" r="5"/><path d="M4 32 Q4 21 14 21 Q24 21 24 32 Q24 21 34 21 Q44 21 44 32"/><rect x="10" y="34" width="28" height="8"/></svg>
    <h3>THERAPIES</h3>
    <p>Class aptent taciti sociosqu ad litora torquent per conubia nostra inceptos</p>
    <span class="go"></span>
  </div>
  <div class="service">
    <svg class="icon" viewBox="0 0 48 48"><circle cx="24" cy="24" r="19"/><path d="M18 19 Q18 13 24 13 Q30 13 30 19 Q30 23 24 25 L24 30"/><circle cx="24" cy="35" r="1.5"/></svg>
    <h3>ABOUT KOLREV</h3>
    <p>Class aptent taciti sociosqu ad litora torquent per conubia nostra inceptos</p>
    <span class="go"></span>
  </div>
  <div class="service">
    <svg class="icon" viewBox="0 0 48 48"><circle cx="22" cy="8" r="4"/><path d="M22 13 L22 26 L34 26 L38 38"/><circle cx="20" cy="32" r="10"/></svg>
    <h3>DISABILITY</h3>
    <p>Class aptent taciti sociosqu ad litora torquent per conubia nostra inceptos</p>
    <span class="go"></span>
  </div>
  <div class="service">
    <svg class="icon" viewBox="0 0 48 48"><path d="M6 42 L6 20 L24 8 L42 20 L42 42 Z"/><rect x="19" y="28" width="10" height="14"/><rect x="11" y="24" width="5" height="5"/><rect x="32" y="24" width="5" height="5"/></svg>
    <h3>SCHOOL</h3>
    <p>Class aptent taciti sociosqu ad litora torquent per conubia nostra inceptos</p>
    <span class="go"></span>
  </div>
</section>

<section class="news">
  <h2 class="section-title">LATEST NEWS</h2>
  <span class="rule"></span>
  <div class="news-list">
    <article class="news-card">
      <div class="news-photo" role="img" aria-label="Photo of a counsellor talking with a young client"></div>
      <div class="news-body">
        <span class="news-date">2018-12-03</span>
        <h4>Morbi porta libero nibh</h4>
        <p>Aliquam libero nisl suscipit vitae placerat et luctus in quam sed mattis</p>
        <span class="read-more">READ MORE</span>
      </div>
    </article>
    <article class="news-card">
      <div class="news-photo" role="img" aria-label="Photo of a group meeting around a table"></div>
      <div class="news-body">
        <span class="news-date">2018-12-03</span>
        <h4>Class aptent taciti sociosqu</h4>
        <p>Aliquam libero nisl suscipit vitae placerat et luctus in quam sed mattis</p>
        <span class="read-more">READ MORE</span>
      </div>
    </article>
    <article class="news-card">
      <div class="news-photo" role="img" aria-label="Photo of a young woman in a conversation"></div>
      <div class="news-body">
        <span class="news-date">2018-12-03</span>
        <h4>Vivamus porttitor purus nis</h4>
        <p>Aliquam libero nisl suscipit vitae placerat et luctus in quam sed mattis</p>
        <span class="read-more">READ MORE</span>
      </div>
    </article>
  </div>
</section>

<section class="testimonials">
  <h2>TESTIMONIALS</h2>
  <div class="rule"></div>
  <div class="quote-mark">&ldquo;</div>
  <blockquote>Aeleuada iaculis ipsum dui aliquet felis at cursus magna nisl vel elit. Praesent elementum elit at tellus nec ultricies sit amet porttitor mattis enim in massa libero interdum nec.</blockquote>
  <p class="author">BY AUTHOR NAME</p>
  <svg class="arrow" style="left:160px" viewBox="0 0 30 30"><path d="M26 15 H4 M12 7 L4 15 L12 23"/></svg>
  <svg class="arrow" style="right:160px" viewBox="0 0 30 30"><path d="M4 15 H26 M18 7 L26 15 L18 23"/></svg>
</section>

<section class="careers" role="img" aria-label="Photo of many hands stacked together in teamwork">
  <svg class="hexagon" viewBox="0 0 320 350"><polygon points="160,0 320,88 320,262 160,350 0,262 0,88" fill="#f04a50"/></svg>
  <div class="hex-content">
    <h2>WORK WITH US</h2>
    <p>Morbi porta libero nibh vitae placerat nunc cursus sed gravida mauris eget tincidunt ante</p>
    <span class="btn btn-outline">CLICK HERE</span>
  </div>
</section>

<footer class="site-footer">
  <div class="footer-brand"><span class="brand-dot"></span><span class="brand-name">Kolrev</span></div>
  <div class="footer-col" style="left:420px">
    <h4>QUICK LINKS</h4>
    <ul><li>Home</li><li>About Kolrev</li><li>Ekbacken Kolrev</li><li>Work with us</li><li>plug</li></ul>
  </div>
  <div class="footer-col" style="left:600px">
    <h4>RESOURCES</h4>
    <ul><li>010-4471930</li><li>info@kolrev.se</li><li>Mon - Fri 9:00 - 16:00</li></ul>
    <div class="social"><span></span><span></span><span></span></div>
  </div>
  <div class="footer-col" style="left:800px">
    <h4>NEWSLETTER</h4>
    <div class="newsletter-input">Email address</div>
    <span class="btn btn-red">SUBSCRIBE</span>
  </div>
</footer>
<div class="copyright">© 2018 Company Name. All right reserved</div>

</body>
</html>
```